Banner signature

Hi, looking for a banner for email signature 728 px wide and 200 px high
Could we have our 10 year logo and premium logo, a similar look and feel of our previous banner design (I've attached) and also include an aboriginal design with the Wording
This email comes to you from Gubbi Gubbi country
I've attached an example of some look and feels that we like.
Can we have the background of banner the Blue colour of our Fern & Harbor logo and

```html
<!DOCTYPE html>
<html lang="en">
<head>
<meta charset="utf-8">
<title>Email Signature Banner</title>
<link rel="stylesheet" href="https://fonts.googleapis.com/css2?family=Exo+2:wght@600&family=Kalam:wght@700&display=swap">
<style>
  :root {
    --stage: #29baff;
    --banner-deep: #0d4a86;
    --banner-mid: #14589a;
    --banner-glow: #2a7fc0;
    --white: #ffffff;
    --stripe: #3fb3ea;
    --gold: #d9ac3a;
    --gold-light: #f3d77a;
    --ribbon: #5cc3ee;
    --ribbon-tail: #c7952f;
  }
  html, body {
    margin: 0;
    width: 1200px;
    height: 1200px;
    overflow: hidden;
    background: var(--stage);
  }
  .banner {
    position: absolute;
    left: 163px;
    top: 480px;
    width: 874px;
    height: 240px;
    overflow: hidden;
    background: linear-gradient(160deg, var(--banner-deep) 0%, var(--banner-mid) 55%, var(--banner-glow) 85%, var(--banner-mid) 100%);
  }
  .banner__pattern {
    position: absolute;
    inset: 0;
    background: radial-gradient(ellipse at 70% 20%, rgba(60, 170, 230, 0.18), transparent 60%);
  }
  .banner__side {
    position: absolute;
    inset: 0;
  }
  .seal {
    position: absolute;
    border-radius: 50%;
    background: radial-gradient(circle at 40% 35%, var(--gold-light), var(--gold) 70%);
  }
  .seal--anniversary {
    left: 59px;
    top: 42px;
    width: 156px;
    height: 156px;
  }
  .message {
    position: absolute;
    left: 469px;
    top: 0;
    transform: translateX(-50%);
    text-align: center;
    color: var(--white);
    white-space: nowrap;
  }
  .message__lead {
    display: block;
    margin-top: 52px;
    font: 700 24px/1 "Kalam", cursive;
  }
  .message__place {
    display: block;
    margin-top: 6px;
    font: 600 56px/1 "Exo 2", sans-serif;
    letter-spacing: 1px;
  }
  .message__tail {
    display: block;
    margin-top: -2px;
    margin-left: 30px;
    font: 700 27px/1 "Kalam", cursive;
  }
  .premium {
    position: absolute;
    left: 731px;
    top: 22px;
    width: 96px;
    height: 96px;
    border-radius: 50%;
    background: radial-gradient(circle at 40% 35%, var(--gold-light), var(--gold) 70%);
    display: flex;
    align-items: center;
    justify-content: center;
    text-align: center;
    font: 600 13px/1.1 "Exo 2", sans-serif;
    color: var(--banner-deep);
  }
</style>
</head>
<body>
  <section class="banner" aria-label="Email signature banner">
    <div class="banner__pattern" role="img" aria-label="Aboriginal dot-circle artwork across the banner"></div>

    <svg class="banner__side" width="874" height="240" viewBox="0 0 874 240" aria-hidden="true">
      <polygon points="0,0 218,0 122,240 0,240" fill="var(--white)"/>
      <polygon points="120,0 132,0 20,240 8,240" fill="var(--stripe)"/>
      <polygon points="142,0 150,0 40,240 32,240" fill="var(--stripe)"/>
      <polygon points="160,0 170,0 62,240 52,240" fill="var(--stripe)"/>
      <polygon points="749,0 818,0 818,164 784,148 749,164" fill="var(--ribbon)"/>
      <polygon points="784,148 818,164 818,160" fill="var(--ribbon-tail)"/>
      <polygon points="790,120 818,120 818,164 790,152" fill="var(--ribbon-tail)"/>
      <polygon points="749,0 818,0 818,164 784,148 749,164" fill="var(--ribbon)"/>
    </svg>

    <div class="seal seal--anniversary" aria-label="Anniversary badge"></div>

    <p class="message">
      <span class="message__lead">This email comes to you from</span>
      <span class="message__place">Gubbi Gubbi</span>
      <span class="message__tail">country</span>
    </p>

    <div class="premium">Fern &amp;<br>Harbor</div>
  </section>
</body>
</html>
```